TELVA EV

We need a business card design for a new Luxury golf cart Company Telva. We manufacture and sell high end golf carts. We would like to see designs that are high end. I have the logo so really need a nice clean look.

```html
<!DOCTYPE html>
<html lang="en">
<head>
<meta charset="utf-8">
<title>Telva EV Business Card</title>
<link rel="stylesheet" href="https://fonts.googleapis.com/css2?family=Saira:wght@400;700&display=swap">
<style>
  :root {
    --page-bg: #e9e9e9;
    --card-bg: #060709;
    --silver: #cfcfcf;
    --silver-line: #bdbdbd;
    --white: #ffffff;
    --teal: #1a9c80;
  }
  * { margin: 0; padding: 0; box-sizing: border-box; }
  html, body {
    width: 1200px;
    height: 1200px;
    overflow: hidden;
    background: var(--page-bg);
  }
  body {
    position: relative;
    font-family: "Saira", sans-serif;
  }
  .card {
    position: absolute;
    left: 155px;
    width: 888px;
    height: 520px;
    background: var(--card-bg);
    box-shadow: 0 1px 3px rgba(0,0,0,0.25);
  }
  .card--front { top: 61px; }
  .card--back { top: 611px; }

  .wordmark {
    position: absolute;
    transform: translate(-50%, -50%);
    font-family: "Saira", sans-serif;
    font-weight: 700;
    color: var(--silver);
    letter-spacing: 0.04em;
    line-height: 1;
    white-space: nowrap;
  }
  .card--front .wordmark {
    left: 245px;
    top: 261px;
    font-size: 64px;
  }
  .card--back .wordmark {
    left: 444px;
    top: 260px;
    font-size: 112px;
  }

  .contact-panel {
    position: absolute;
    left: 477px;
    top: 109px;
    width: 358px;
    height: 302px;
    border: 2.5px solid var(--silver-line);
    border-radius: 22px;
  }
  .person {
    position: absolute;
    right: 48px;
    top: 52px;
    text-align: right;
  }
  .person__name {
    color: var(--white);
    font-weight: 700;
    font-size: 38px;
    line-height: 1;
    letter-spacing: 0.02em;
  }
  .person__role {
    color: var(--white);
    font-weight: 400;
    font-size: 18px;
    line-height: 1;
    margin-top: 6px;
    letter-spacing: 0.04em;
  }
  .contact-list {
    position: absolute;
    right: 18px;
    top: 160px;
    list-style: none;
  }
  .contact-list__item {
    display: flex;
    align-items: center;
    justify-content: flex-end;
    height: 29px;
    color: var(--white);
    font-size: 20px;
    font-weight: 400;
    letter-spacing: 0.03em;
  }
  .contact-list__icon {
    width: 14px;
    height: 14px;
    margin-left: 14px;
    fill: var(--teal);
  }
</style>
</head>
<body>

<section class="card card--front" aria-label="Business card front">
  <div class="wordmark">TELVA</div>

  <div class="contact-panel">
    <div class="person">
      <div class="person__name">Martin Hale</div>
      <div class="person__role">Founder</div>
    </div>
    <ul class="contact-list">
      <li class="contact-list__item">044 3719 0000
        <svg class="contact-list__icon" viewBox="0 0 24 24" aria-hidden="true">
          <path d="M6.6 10.8a15.1 15.1 0 0 0 6.6 6.6l2.2-2.2c.3-.3.7-.4 1-.2 1.1.4 2.3.6 3.6.6.6 0 1 .4 1 1V20c0 .6-.4 1-1 1A17 17 0 0 1 3 4c0-.6.4-1 1-1h3.5c.6 0 1 .4 1 1 0 1.3.2 2.5.6 3.6.1.3 0 .7-.2 1z"/>
        </svg>
      </li>
      <li class="contact-list__item">info@telvanet
        <svg class="contact-list__icon" viewBox="0 0 24 24" aria-hidden="true">
          <path d="M2 5h20v14H2z M4 7v.4l8 5 8-5V7l-8 5z" fill-rule="evenodd"/>
        </svg>
      </li>
      <li class="contact-list__item">www.atelva.net
        <svg class="contact-list__icon" viewBox="0 0 24 24" aria-hidden="true">
          <path d="M12 2a10 10 0 1 0 0 20 10 10 0 0 0 0-20zm6.9 6h-3a15.7 15.7 0 0 0-1.4-3.6A8 8 0 0 1 18.9 8zM12 4c.8 1.2 1.5 2.5 1.9 4h-3.8c.4-1.5 1.1-2.8 1.9-4zM4.3 14a8.2 8.2 0 0 1 0-4h3.4a16.5 16.5 0 0 0 0 4zm.8 2h3c.3 1.3.8 2.5 1.4 3.6A8 8 0 0 1 5.1 16zm3-8h-3a8 8 0 0 1 4.4-3.6C8.9 5.5 8.4 6.7 8.1 8zM12 20c-.8-1.2-1.5-2.5-1.9-4h3.8c-.4 1.5-1.1 2.8-1.9 4zm2.3-6H9.7a14.7 14.7 0 0 1 0-4h4.6a14.7 14.7 0 0 1 0 4zm.2 5.6c.6-1.1 1.1-2.3 1.4-3.6h3a8 8 0 0 1-4.4 3.6zm1.8-5.6a16.5 16.5 0 0 0 0-4h3.4a8.2 8.2 0 0 1 0 4z"/>
        </svg>
      </li>
    </ul>
  </div>
</section>

<section class="card card--back" aria-label="Business card back">
  <div class="wordmark">TELVA</div>
</section>

</body>
</html>
```